Update to Current Website (www.lrcapitalplanning.example)

5 pages is what I need. This is one cohesive design across all pages.

I would like to create an update to the current website with a fresh look and feel that is mobile compatible.

All content will stay the same. The only thing I want removed from the current content is "Returns for every turning chapter" that is on the main page.

The website address is www.lrcapitalplanning.example

need the site to be mobile-optimized/responsive

During the contest, you can submit one design or page, and in the handover, once selected, the winner will provide the rest of the pages.

Updates

This has been upgraded to a coded project. Looking for something clean, professional, and goes with my newly designed logo. Please read brief for details! Added Monday, February 1, 2016

Target Market(s)

Consumers

Industry/Entity Type

Financial Planning

Coding

Coded - Design and coding required

Number of Pages Required

5+ page

Requirements
Must have
• Really like pagelatticer builder Harlow Template or www.silverbirchcounsel.example
• Something eye catching, simple, and easy to navigate

```html
<!DOCTYPE html>
<html lang="en">
<head>
<meta charset="utf-8">
<title>L&amp;R Wealth Management</title>
<link href="https://fonts.googleapis.com/css2?family=Rajdhani:wght@500;600&family=Arimo:wght@400;700&display=swap" rel="stylesheet">
<style>
:root{
  --orange:#d68a1c;
  --orange-dark:#b97313;
  --ink:#222;
  --body:#444;
  --nav:#2b2b2b;
  --footer:#222;
  --footer-text:#e6e6e6;
  --rule:#ddd;
  --head:'Rajdhani',sans-serif;
  --text:'Arimo',Arial,sans-serif;
}
*{box-sizing:border-box;margin:0;padding:0}
html,body{width:954px;height:1200px;overflow:hidden;background:#fff}
body{position:relative;font-family:var(--text);color:var(--body)}
.abs{position:absolute}

.site-header{position:absolute;left:0;top:0;width:954px;height:92px;background:#fbf8f4}
.brand{left:90px;top:18px;font-family:var(--head);font-weight:600;font-size:27px;color:var(--ink);line-height:1;display:flex;align-items:center;gap:8px}
.brand .mark{width:16px;height:16px;border-radius:50%;background:var(--orange)}
.brand-sub{left:114px;top:52px;font-family:var(--head);font-weight:600;font-size:13px;color:var(--ink);letter-spacing:.5px}
.badge{left:438px;top:8px;width:80px;height:44px;background:#fff;border:2px solid #1d2f4d;border-bottom:8px solid #c0272d}
.contact-top{top:24px;display:flex;align-items:center;gap:6px;font-family:var(--head);font-weight:500;color:var(--ink)}
.contact-top.phone{left:556px;font-size:17px}
.contact-top.mail{left:688px;font-family:var(--text);font-size:11px}
.main-nav{left:410px;top:57px;width:544px;height:35px;background:var(--nav);clip-path:polygon(20px 0,100% 0,100% 100%,0 100%)}
.main-nav a{position:absolute;top:0;height:35px;line-height:35px;color:#fff;text-decoration:none;font-family:var(--head);font-weight:500;font-size:13px}
.main-nav a.active{top:8px;height:20px;line-height:20px;padding:0 7px;background:var(--orange)}
.main-nav .sep{position:absolute;top:0;width:1px;height:35px;background:#444}

.hero{left:0;top:92px;width:954px;height:339px;background:linear-gradient(100deg,#2a2c33 0%,#5a4d4a 30%,#b7a89a 55%,#8f8374 70%,#3a3a40 100%)}
.hero-caption{left:0;top:398px;width:954px;height:33px;background:rgba(20,20,20,.75);color:#fff;text-align:center;font-family:var(--head);font-weight:500;font-size:17px;line-height:33px}
.arrow{top:218px;width:33px;height:27px;background:#2a2a2a;border:2px solid #bbb;display:flex;align-items:center;justify-content:center}

.service{top:466px;width:228px;height:260px;border:1px solid #e3e3e3;text-align:center}
.service .icon{margin:13px auto 0;width:96px;height:96px;border-radius:50%;border:2px solid var(--orange);padding:4px}
.service .icon div{width:100%;height:100%;border-radius:50%;background:var(--orange);display:flex;align-items:center;justify-content:center}
.service h3{margin-top:9px;font-family:var(--head);font-weight:500;font-size:18px;color:var(--ink)}
.service p{margin:12px 18px 0;font-size:10.5px;line-height:17px}
.read-more{display:inline-block;font-size:10.5px;color:var(--orange);text-decoration:underline}
.service .read-more{margin-top:10px}

.welcome-title{left:0;top:756px;width:954px;text-align:center;font-family:var(--head);font-weight:500;font-size:21px;color:var(--ink)}
.welcome-title span{display:inline-block;width:12px;height:12px;border-radius:50%;background:var(--orange);margin-right:10px}
.welcome-rule{left:256px;top:791px;width:442px;height:1px;background:var(--rule)}
.welcome-accent{left:449px;top:790px;width:55px;height:3px;background:var(--orange)}
.welcome-text{left:102px;top:804px;width:750px;text-align:center;font-size:10.5px;line-height:17.5px}
.welcome-more{left:0;top:892px;width:954px;text-align:center}

.site-footer{left:0;top:937px;width:954px;height:194px;background:var(--footer);color:var(--footer-text)}
.col{position:absolute;top:26px}
.col h4{font-family:var(--head);font-weight:500;font-size:14px;color:#fff;padding-bottom:6px;border-bottom:1px dotted #555}
.col h4 em{font-style:normal;color:var(--orange)}
.col-sep{position:absolute;top:30px;width:1px;height:120px;background:#333}
.links li{list-style:none;font-size:10px;margin-top:9px;padding-left:16px;position:relative;line-height:12px}
.links li::before{content:"›";position:absolute;left:0;color:#aaa}
.info{font-size:10px;line-height:13.5px;display:flex;gap:8px;margin-top:12px}
.info svg{flex:none}
.news p{font-size:9.5px;line-height:13.5px;margin-top:12px}
.news .field{margin-top:9px;width:184px;height:29px;background:#444;color:#ddd;font-size:9.5px;line-height:29px;padding-left:8px}
.news .btn{margin-top:10px;width:83px;height:29px;background:var(--orange);color:#fff;font-family:var(--head);font-weight:600;font-size:16px;line-height:29px;text-align:center}
.social{display:flex;gap:8px;margin-top:13px}
.social span{width:24px;height:24px;border-radius:50%;background:#5a4a35}
.foot-brand{margin-top:14px;font-family:var(--head);font-weight:600;font-size:20px;color:#ccc;text-align:center}

.legal{left:0;top:1131px;width:954px;height:69px;background:var(--orange);color:#fff;text-align:center}
.legal .copy{margin-top:8px;font-family:var(--head);font-weight:500;font-size:13px;color:#2a2a2a}
.legal .note{margin:6px auto 0;width:760px;font-size:9px;line-height:14px}
</style>
</head>
<body>
<header class="site-header">
  <div class="abs brand"><span class="mark"></span>L&amp;R</div>
  <div class="abs brand-sub">WEALTH MANAGEMENT</div>
  <div class="abs badge" role="img" aria-label="Award badge"></div>
  <div class="abs contact-top phone">
    <svg width="18" height="18" viewBox="0 0 18 18"><circle cx="9" cy="9" r="8" fill="none" stroke="#d68a1c" stroke-width="1.5"/><path d="M6 5l2 2-1 1.5c.6 1.2 1.3 1.9 2.5 2.5L11 10l2 2-1.5 1.5C8.5 13 5 9.5 4.5 6.5z" fill="#d68a1c"/></svg>
    555-014-2290
  </div>
  <div class="abs contact-top mail">
    <svg width="20" height="14" viewBox="0 0 20 14"><rect x="1" y="1" width="18" height="12" fill="none" stroke="#d68a1c" stroke-width="1.5"/><path d="M1 1l9 7 9-7" fill="none" stroke="#d68a1c" stroke-width="1.5"/></svg>
    inquiry@lrwealth.example
  </div>
  <nav class="abs main-nav">
    <a class="active" style="left:29px">Home</a>
    <span class="sep" style="left:95px"></span>
    <a style="left:112px">About Us</a>
    <span class="sep" style="left:181px"></span>
    <a style="left:201px">Services</a>
    <span class="sep" style="left:267px"></span>
    <a style="left:287px">Our Team</a>
    <span class="sep" style="left:359px"></span>
    <a style="left:381px">Contact Us</a>
  </nav>
</header>

<div class="abs hero" role="img" aria-label="Photo of an advisor meeting with clients in a bright office"></div>
<div class="abs arrow" style="left:0"><svg width="8" height="10" viewBox="0 0 8 10"><path d="M6 1L2 5l4 4" fill="none" stroke="#fff" stroke-width="2"/></svg></div>
<div class="abs arrow" style="left:917px"><svg width="8" height="10" viewBox="0 0 8 10"><path d="M2 1l4 4-4 4" fill="none" stroke="#fff" stroke-width="2"/></svg></div>
<div class="abs hero-caption">Our Mission Is To Offer Independent &amp; Unbiased Wealth Strategies To Individuals, Families &amp; Businesses</div>

<section class="abs service" style="left:96px">
  <div class="icon"><div><svg width="44" height="40" viewBox="0 0 44 40"><rect x="2" y="22" width="5" height="14" fill="#fff"/><rect x="10" y="16" width="5" height="20" fill="#fff"/><rect x="18" y="12" width="5" height="24" fill="#fff"/><path d="M3 18l9-8 6 4 10-9" fill="none" stroke="#fff" stroke-width="2"/><circle cx="30" cy="24" r="6" fill="none" stroke="#fff" stroke-width="3"/><path d="M34 29l6 7" stroke="#fff" stroke-width="4"/></svg></div></div>
  <h3>Assest Management</h3>
  <p>Lorem ipsum dolor sit amet, consectetuer adipiscing elit, sed diam nonummy nibh euismod tincidunt ut laoreet dolore magna aliquam erat volutpat.</p>
  <a class="read-more">Read More</a>
</section>
<section class="abs service" style="left:363px">
  <div class="icon"><div><svg width="48" height="44" viewBox="0 0 48 44"><path d="M4 16a16 13 0 0 1 32 0z" fill="#fff"/><path d="M20 16v14a3 3 0 0 1-6 0" fill="none" stroke="#fff" stroke-width="2"/><path d="M22 30l12-10 12 10v12H22z" fill="#fff"/><rect x="31" y="34" width="6" height="8" fill="#d68a1c"/><circle cx="20" cy="9" r="5" fill="#d68a1c"/></svg></div></div>
  <h3>Estate &amp; Financial Planning</h3>
  <p>Lorem ipsum dolor sit amet, consectetuer adipiscing elit, sed diam nonummy nibh euismod tincidunt ut laoreet dolore magna aliquam erat volutpat.</p>
  <a class="read-more">Read More</a>
</section>
<section class="abs service" style="left:629px">
  <div class="icon"><div><svg width="40" height="48" viewBox="0 0 40 48"><circle cx="10" cy="6" r="5" fill="#fff"/><path d="M4 14h12v16h-2v16H8V30H4z" fill="#fff"/><circle cx="28" cy="30" r="10" fill="#fff"/><path d="M24 18h8l-2 4h-4z" fill="#fff"/><text x="28" y="35" font-family="Arial" font-weight="700" font-size="13" fill="#d68a1c" text-anchor="middle">$</text></svg></div></div>
  <h3>Investment Approach</h3>
  <p>Lorem ipsum dolor sit amet, consectetuer adipiscing elit, sed diam nonummy nibh euismod tincidunt ut laoreet dolore magna aliquam erat volutpat.</p>
  <a class="read-more">Read More</a>
</section>

<h2 class="abs welcome-title"><span></span>Welcome To L&amp;R Wealth Management</h2>
<div class="abs welcome-rule"></div>
<div class="abs welcome-accent"></div>
<p class="abs welcome-text">Lorem ipsum dolor sit amet, consectetuer adipiscing elit, sed diam nonummy nibh euismod tincidunt ut laoreet dolore magna aliquam erat volutpat. Ut wisi enim ad minim veniam, quis nostrud exerci tation ullamcorper suscipit lobortis nisl ut aliquip ex ea commodo consequat. Duis autem vel eum iriure dolor in hendrerit in vulputate velit esse molestie consequat, vel illum dolore eu feugiat nulla facilisis at vero eros et accumsan et iusto odio dignissim qui blandit praesent luptatum zzril delenit augue duis dolore te feugait nulla facilisi.</p>
<div class="abs welcome-more"><a class="read-more">Read More</a></div>

<footer class="abs site-footer">
  <div class="col" style="left:94px;width:72px">
    <h4>Quick <em>Links</em></h4>
    <ul class="links"><li>Home</li><li>About Us</li><li>Services</li><li>Our Team</li><li>Contact Us</li></ul>
  </div>
  <span class="col-sep" style="left:201px"></span>
  <div class="col" style="left:239px;width:156px">
    <h4>Contact <em>Details</em></h4>
    <div class="info"><svg width="10" height="14" viewBox="0 0 10 14"><path d="M5 0a5 5 0 0 1 5 5c0 4-5 9-5 9S0 9 0 5a5 5 0 0 1 5-5z" fill="#d68a1c"/><circle cx="5" cy="5" r="2" fill="#222"/></svg><span>Street Name, City Name<br>State Zipcode</span></div>
    <div class="info"><svg width="10" height="10" viewBox="0 0 10 10"><path d="M1 1h3l1 2-1.5 1c.6 1.2 1.3 1.9 2.5 2.5L7 5l2 1v3C5 9 1 5 1 1z" fill="#d68a1c"/></svg><span>555-014-2290</span></div>
    <div class="info"><svg width="10" height="10" viewBox="0 0 10 10"><path d="M1 1h3l1 2-1.5 1c.6 1.2 1.3 1.9 2.5 2.5L7 5l2 1v3C5 9 1 5 1 1z" fill="#d68a1c"/></svg><span>555-014-2290 (TF)</span></div>
    <div class="info"><svg width="11" height="8" viewBox="0 0 11 8"><rect width="11" height="8" fill="#d68a1c"/><path d="M0 0l5.5 4L11 0" fill="none" stroke="#222"/></svg><span>inquiry@lrwealth.example</span></div>
  </div>
  <span class="col-sep" style="left:429px"></span>
  <div class="col news" style="left:466px;width:186px">
    <h4>Newsletter <em>Signup</em></h4>
    <p>Sign up for our newsletter and receive new cases as we write them.</p>
    <div class="field">email address</div>
    <div class="btn">SUBMIT</div>
  </div>
  <span class="col-sep" style="left:693px"></span>
  <div class="col" style="left:732px;width:130px">
    <h4>Social <em>Connect</em></h4>
    <div class="social"><span></span><span></span><span></span><span></span></div>
    <div class="foot-brand">L&amp;R Wealth Management</div>
  </div>
</footer>

<div class="abs legal">
  <p class="copy">Copyright © 2016 L&amp;R Wealth Management &nbsp;&nbsp;All Right Reserved</p>
  <p class="note">Securities &amp; Financial Planning offered through Northgate Securities, Member NSRB/ICPF. The Northgate Securities rep. associated with this website may discuss and/or transact securities businees only with residents of the following states: AZ, CA, CO, FL, GA, IA, LA, MA, MN, NV, NY, OK, PA, TN, UT, VA, WA, WI</p>
</div>
</body>
</html>
```